Bikes for Dreams - Website Redesign

Create a professional website for a nonprofit; BikesforDreams.org
Please see boatsforheroes.org and www.pedalsforhopes.org for the concept I am after.
The webpage should have a fun feel and should match the style of the company at www.pedalsforhopes.org. The pages to include are 'Home', 'About us' and 'Get Started'
Thank you and good luck!
Reason: i would like to see more designs.

```html
<!DOCTYPE html>
<html lang="en">
<head>
<meta charset="utf-8">
<title>Bikes for Dreams</title>
<link rel="stylesheet" href="https://fonts.googleapis.com/css2?family=Roboto:wght@400;500&family=Open+Sans:ital,wght@0,400;1,400&display=swap">
<style>
:root{
  --blue:#34499a;
  --band:#3a55a5;
  --orange:#fa7f1b;
  --ink:#2e2e2e;
  --topbar:#3b3b3b;
  --footer:#141414;
  --grey-icon:#dadada;
  --icon-fill:#8a8a8a;
  --text:#555;
  --field-border:#d6d6d6;
}
*{box-sizing:border-box;margin:0;padding:0}
html,body{width:1200px;height:1188px;overflow:hidden;background:#fff}
body{position:relative;font-family:"Open Sans",sans-serif;color:var(--text)}
.topbar{position:absolute;left:0;top:0;width:1200px;height:24px;background:var(--topbar);color:#fff;font:400 10px "Roboto",sans-serif}
.topbar .info{position:absolute;top:6px}
.topbar .social{position:absolute;right:152px;top:6px;display:flex;gap:10px}
.topbar .social span{width:11px;height:11px;background:#fff;border-radius:2px;opacity:.9}
.header{position:absolute;left:0;top:24px;width:1200px;height:59px;background:#fff;border-bottom:1px solid #eee}
.brand{position:absolute;left:150px;top:18px;display:flex;align-items:center;gap:9px}
.brand .mark{width:16px;height:16px;background:var(--orange)}
.brand .name{font:400 20px "Roboto",sans-serif;color:var(--ink);letter-spacing:.2px}
.nav{position:absolute;left:851px;top:0;height:59px;display:flex;font:400 11.5px "Roboto",sans-serif}
.nav a{display:flex;align-items:center;padding:0 15px;color:#666;text-decoration:none;border-right:1px solid #eee;height:59px}
.nav a.active{background:var(--orange);color:#fff;width:52px;padding:0;justify-content:center}
.nav a:last-child{border:0}
.hero{position:absolute;left:0;top:83px;width:1200px;height:555px;background:radial-gradient(ellipse at 45% 40%,#b58f78 0%,#6b625c 35%,#4a5158 60%,#9fb9bd 85%,#c7dbdd 100%)}
.arrow{position:absolute;top:290px}
.form-panel{position:absolute;left:783px;top:39px;width:266px;height:484px;background:rgba(243,243,243,.96)}
.form-panel h2{position:absolute;left:20px;top:20px;font:500 19.5px "Roboto",sans-serif;color:var(--blue);white-space:nowrap}
.form-panel h3{position:absolute;left:20px;top:275px;font:500 14.5px "Roboto",sans-serif;color:var(--blue);white-space:nowrap}
.accent{color:var(--orange)}
.field{position:absolute;left:18px;width:225px;height:32px;background:#fff;border:1px solid var(--field-border);border-radius:3px;font:400 11.5px "Roboto",sans-serif;color:#888;padding:9px 8px}
.submit{position:absolute;left:16px;top:435px;width:230px;height:31px;background:var(--orange);border-radius:4px;color:#fff;font:500 14px "Roboto",sans-serif;text-align:center;line-height:31px}
.feature{position:absolute;top:670px;width:240px;text-align:center}
.feature .badge{width:120px;height:120px;border-radius:50%;background:var(--grey-icon);margin:0 auto;display:flex;align-items:center;justify-content:center}
.feature .badge.on{background:var(--orange)}
.feature h4{margin-top:12px;font:500 17.5px "Roboto",sans-serif;color:var(--blue);white-space:nowrap}
.feature p{margin-top:4px;font-size:12px;line-height:18px;color:var(--text)}
.newsletter{position:absolute;left:0;top:929px;width:1200px;height:84px;background:var(--band)}
.newsletter .title{position:absolute;left:237px;top:27px;font:400 24px "Open Sans",sans-serif;color:#fff;white-space:nowrap}
.newsletter .email{position:absolute;left:581px;top:19px;width:291px;height:48px;background:#fff;border-radius:3px 0 0 3px;font:italic 12.5px "Open Sans",sans-serif;color:#999;padding:15px 12px}
.newsletter .btn{position:absolute;left:872px;top:19px;width:141px;height:48px;background:var(--orange);color:#fff;font:400 15px "Roboto",sans-serif;text-align:center;line-height:48px;border-radius:0 3px 3px 0}
.footer{position:absolute;left:0;top:1013px;width:1200px;height:175px;background:var(--footer);color:#fff;text-align:center}
.footer h5{position:absolute;left:0;width:1200px;top:28px;font:400 16.5px "Roboto",sans-serif}
.footer .dots{position:absolute;left:548px;top:59px;display:flex;gap:7px}
.footer .dots span{width:21px;height:21px;border-radius:50%;background:#fff}
.footer .links{position:absolute;left:0;width:1200px;top:94px;font-size:11px}
.footer hr{position:absolute;left:189px;top:119px;width:823px;border:0;border-top:1px solid #555}
.footer .copy{position:absolute;left:0;width:1200px;top:144px;font-size:10px}
</style>
</head>
<body>
<div class="topbar">
  <span class="info" style="left:150px">Call toll-free 1-800-555-0142</span>
  <span class="info" style="left:305px">Live operators - 7 days a week</span>
  <div class="social"><span></span><span></span><span></span><span></span></div>
</div>
<header class="header">
  <div class="brand"><span class="mark"></span><span class="name">Bikes for Dreams</span></div>
  <nav class="nav"><a class="active" href="#">HOME</a><a href="#">About Us</a><a href="#">Get Started</a></nav>
</header>
<section class="hero" role="img" aria-label="Photo of a smiling man leaning against a car door">
  <svg class="arrow" style="left:92px" width="20" height="36"><path d="M18 2 2 18l16 16" fill="none" stroke="rgba(255,255,255,.35)" stroke-width="2"/></svg>
  <svg class="arrow" style="left:1074px" width="20" height="36"><path d="M2 2l16 16L2 34" fill="none" stroke="#fff" stroke-width="2"/></svg>
  <form class="form-panel">
    <h2>DONATION PICK <span class="accent">UP FORM</span></h2>
    <div class="field" style="top:58px">First Name:</div>
    <div class="field" style="top:100px">Last Name:</div>
    <div class="field" style="top:143px">Zip Code:</div>
    <div class="field" style="top:185px">Email Address:</div>
    <div class="field" style="top:228px">Day Phone:</div>
    <h3>VEHICLE DONATION INFORMATION</h3>
    <div class="field" style="top:303px">Year of Vehicle:</div>
    <div class="field" style="top:345px">Make of Vehicle:</div>
    <div class="field" style="top:388px">Model of Vehicle:</div>
    <div class="submit">SUBMIT YOUR APPLICATION</div>
  </form>
</section>

<div class="feature" style="left:112px">
  <div class="badge on"><svg width="80" height="70" viewBox="0 0 80 70"><path d="M8 6l10 16" stroke="#fff" stroke-width="5"/><circle cx="30" cy="40" r="11" fill="none" stroke="#fff" stroke-width="5"/><path d="M45 30l30 14v22L45 40z" fill="#fff"/></svg></div>
  <h4>FREE LOCAL TOWING</h4>
  <p>Running or not, Any Condition<br>&amp; Pickup Anywhere.</p>
</div>
<div class="feature" style="left:331px">
  <div class="badge"><svg width="80" height="62" viewBox="0 0 80 62"><rect x="2" y="2" width="44" height="44" fill="var(--icon-fill)"/><path d="M48 14h16l14 14v18H48z" fill="var(--icon-fill)"/><circle cx="17" cy="52" r="8" fill="var(--icon-fill)" stroke="var(--grey-icon)" stroke-width="3"/><circle cx="62" cy="52" r="8" fill="var(--icon-fill)" stroke="var(--grey-icon)" stroke-width="3"/></svg></div>
  <h4>FAST PICKUP</h4>
  <p>Same Day to 24 Hours.</p>
</div>
<div class="feature" style="left:553px">
  <div class="badge"><svg width="80" height="70" viewBox="0 0 80 70"><path d="M6 3h44M6 67h44M12 3c0 22 20 24 20 32S12 45 12 67h32c0-22-20-24-20-32S44 25 44 3" fill="none" stroke="var(--icon-fill)" stroke-width="5"/><circle cx="56" cy="48" r="18" fill="var(--icon-fill)" stroke="var(--grey-icon)" stroke-width="3"/><text x="56" y="56" text-anchor="middle" font-family="Roboto,sans-serif" font-weight="500" font-size="22" fill="var(--grey-icon)">$</text></svg></div>
  <h4>INCOME TAX DEDUCTION</h4>
  <p>We issue you an IRS tax receipt &amp; offer<br>the largest resale network to get you the<br>highest tax write-off possible.</p>
</div>
<div class="feature" style="left:820px">
  <div class="badge"><svg width="76" height="76"><circle cx="38" cy="38" r="32" fill="none" stroke="var(--icon-fill)" stroke-width="7"/><path d="M16 60 60 16" stroke="var(--icon-fill)" stroke-width="7"/></svg></div>
  <h4>NO PAPERWORK HASSLES</h4>
  <p>We take any car and handle everything:<br>DMV, Smog, &amp; IRS paperwork.</p>
</div>

<section class="newsletter">
  <svg style="position:absolute;left:189px;top:28px" width="42" height="30" viewBox="0 0 42 30"><rect x="1" y="1" width="40" height="28" fill="#fff"/><path d="M1 1l20 16L41 1M1 29l15-15M41 29 26 14" fill="none" stroke="var(--band)" stroke-width="2"/></svg>
  <div class="title">Subscribe to our Newsletter</div>
  <div class="email">Your Email Address...</div>
  <div class="btn">SUBSCRIBE</div>
</section>

<footer class="footer">
  <h5>CONNECT WITH US</h5>
  <div class="dots"><span></span><span></span><span></span><span></span></div>
  <div class="links">Home &nbsp;| &nbsp;About Us &nbsp;| &nbsp;Get Started</div>
  <hr>
  <div class="copy">© Copyright 2017 Bikes for Dreams . Disclaimer &nbsp;| &nbsp;&nbsp;Privacy &nbsp;| &nbsp;&nbsp;Site Map</div>
</footer>
</body>
</html>
```